We invest in Electric Vehicles and renewable energy - help sell us!

INTRO: We want a PowerPoint template / Master Presentation to be used to sell our company and first investment fund to professional investors and to present ourselves to businesses that will develop the infrastructure projects in which we will invest.

WHO WE ARE: We are a newly created investment advisory and fund management company specialised in sustainable mobility.

WHAT WE DO: We invest in infrastructure projects that provide electric vehicles, charging infrastructure (charging stations etc) and associated renewable energy generation services (eg solar panels on roof-tops and solar parks, wind energy). The users of the projects in which we invest are operators of vehicle fleets (taxis, buses, delivery, which may be for 2, 3 and 4 wheel vehicles from motorbikes through cars, vans, buses and trucks).

PURPOSE OF THE POWERPOINT: We are looking for a presentation (1) to sell our investment services to investors (to raise money) and (2) to present what we do to fleet operators and service providers who will develop the projects.

CONTENT: We need all of the usual front cover slide / content slide / intermediate divider-heading slide / slides that integrate the most common tables, charts and smart graphics / team slide / a variety of text slides / a testimonial slide / Example project slide / Final contact and Disclaimer text slide etc all customised to the design. We rely on your experience for providing the further standard formats and layouts that one might find in a high-quality financial sector corporate presentation deck.

VERSIONS: We want three versions of the slides where there are images (eg front and back covers, section breaks, testimonial slides..). The three could be themed eg (1) futuristic and/or abstract in the theme of our investment scope (2) Street themes with vehicles and people in developed and developing markets (3) a mix of aerial and land-based views of roads (4) more explicit around the types of infrastructure in which we invest (vehicles of different types, charging infrastructure, solar panels on industrial and commercial roof tops etc)

LOOK & FEEL: The presentation must be sleek, dynamic if sober, with a clean feel, it should project an image of clarity and confidence, but also elicit some emotional appeal (even if it is very subtle!) ... we are in the e-mobility sector after all! We have an existing logo (attached).

We have an existing website www.dorelmont.capital (one day it will need an upgrade too!) it may serve as inspiration / allow you better to understand our activities!

SOME PICS THAT WE LIKE: for inspiration only (NON exhaustive!):

• https://www.klipvane.com/video/stock/unrecognizable-highway-traffic-head-on-bgkbvhtcmjn19iqta
• https://www.klipvane.com/video/stock/new-york-city-streets-nt1vyz3
• https://www.klipvane.com/video/stock/4k-time-lapse-of-traffic-speeding-on-a-straight-section-of-highway-during-an-evening-rush-hour-ps1llt0
• https://www.klipvane.com/video/stock/cinematic-urban-aerial-time-lapse-of-city-infrastructure-including-freeways-interstates-roads-streets-with-traffic-at-rush-hour-during-the-evening-bzjhqhqfmjbhns0h9
• https://www.klipvane.com/video/stock/charging-of-electric-car-eco-energy-transport-and-power-supply-environmentally-conscious-transportation-vehicle-plugged-in-charger-terminal-in-the-city-4k-rsl8pukqmejqpaojnn
• https://www.klipvane.com/video/stock/drone-view-of-modern-vehicle-driving-on-road-near-ploughed-field-and-wind-turbine-in-countryside-rzwqrsqvdkg85gavm

FINALLY: note the attached 'slides to include' are additonal slides that we want to be well presented (see additional detail on Slide 1 of the file)

Target Market(s)

Institutional investors (pension funds, asset managers, family offices) & the dreamer in each of us!!

Industry/Entity Type

Financial services (B2B NOT B2C)

Font styles to use
Other font styles liked:
• Calibri but can consider alternatives

Requirements
Must have
• We need all of the usual front cover slide / content slide / intermediate divider-heading slide / slides that integrate the most common tables, charts and smart graphics / team slide / a variety of text slides / a testimonial slide / Example project slide / Final contact and Disclaimer text slide etc all customised to the design. We rely on your experience for providing the further standard formats and layouts that one might find in a high-quality financial sector corporate presentation deck
Nice to have
• Would like to see any other pages that are standard in your experience! Also would like to see one version of the slides with a summary section clearly marked for each slide (with space for text) which will serve for quick reading of the presentation for key points)

```html
<!DOCTYPE html>
<html lang="en">
<head>
<meta charset="utf-8">
<title>Dorelmont Capital – Presentation Template</title>
<link rel="stylesheet" href="https://fonts.googleapis.com/css2?family=Arimo:wght@400&family=Noto+Sans:wght@400&family=Tinos:wght@400&display=swap">
<style>
  :root {
    --stage: #aaaab1;
    --paper: #ffffff;
    --forest: #2a4320;
    --title-green: #2e4a22;
    --leaf: #70a33d;
    --ink: #1e1e1e;
    --muted: #333333;
    --rule: #dcdcdc;
    --chart-bg: #f0efed;
  }
  * { box-sizing: border-box; margin: 0; padding: 0; }
  html, body { width: 1200px; height: 3288px; overflow: hidden; }
  body { background: var(--stage); font-family: "Noto Sans", Verdana, sans-serif; color: var(--ink); position: relative; }

  .slide { position: absolute; left: 106px; width: 1002px; height: 563px; background: var(--paper); overflow: hidden; }
  .slide-title { position: absolute; left: 24px; top: 22px; font-family: "Tinos", "Times New Roman", serif; font-size: 32px; font-weight: 400; color: var(--title-green); }
  .brand { position: absolute; right: 24px; top: 28px; display: flex; align-items: center; gap: 8px; font-family: "Arimo", Arial, sans-serif; font-size: 28px; font-weight: 400; color: var(--title-green); }
  .brand-dot { width: 14px; height: 14px; border-radius: 50%; background: var(--leaf); }
  .photo { position: absolute; }

  /* Intro slide */
  .intro { top: 70px; }
  .intro-panel { position: absolute; left: 27px; top: 105px; width: 490px; height: 414px; background: var(--forest); }
  .intro-icon { position: absolute; left: 28px; width: 66px; height: 66px; border-radius: 50%; background: var(--leaf); display: flex; align-items: center; justify-content: center; }
  .intro-text { position: absolute; left: 117px; width: 300px; font-family: "Arimo", Arial, sans-serif; font-size: 15px; line-height: 20px; color: #ffffff; white-space: nowrap; }
  .intro-photo { left: 439px; top: 134px; width: 534px; height: 356px; background: linear-gradient(180deg, #efe7c0 0%, #d9cf98 30%, #8fae8a 55%, #3f9a9a 75%, #2b7e86 100%); }

  /* Team slide */
  .team { top: 673px; }
  .team .slide-title { left: 29px; }
  .member { position: absolute; top: 79px; width: 230px; height: 451px; border: 1px solid var(--rule); }
  .member-photo { position: absolute; left: 15px; top: 20px; width: 160px; height: 160px; }
  .member-name { position: absolute; left: 15px; top: 211px; font-family: "Tinos", "Times New Roman", serif; font-size: 15px; line-height: 19px; color: var(--ink); }
  .member-bio { position: absolute; left: 15px; top: 257px; width: 200px; font-size: 10.5px; line-height: 14.3px; color: var(--muted); }

  /* Projects slide */
  .projects { top: 1279px; }
  .projects-photo { left: 31px; top: 100px; width: 448px; height: 408px; background: linear-gradient(160deg, #9a8e7e 0%, #6c7c86 35%, #4f8fb0 55%, #c9c27a 75%, #7a7066 100%); }
  .sub-heading { position: absolute; font-family: "Tinos", "Times New Roman", serif; font-size: 25px; font-weight: 400; color: var(--ink); }
  .bullets { position: absolute; list-style: none; }
  .bullets li { position: relative; padding-left: 20px; font-size: 11.5px; line-height: 16px; color: var(--ink); }
  .bullets li::before { content: ""; position: absolute; left: 1px; top: 5px; border-left: 5px solid var(--ink); border-top: 3.5px solid transparent; border-bottom: 3.5px solid transparent; }
  .projects .bullets { left: 523px; top: 188px; width: 445px; }
  .projects .bullets li { margin-bottom: 25px; }
  .projects-note { position: absolute; left: 523px; top: 450px; width: 445px; font-size: 11.5px; line-height: 17px; }

  /* Why partner slide */
  .partner { top: 1891px; }
  .partner .bullets { left: 51px; top: 211px; width: 345px; }
  .partner .bullets li { margin-bottom: 26px; }
  .bar-chart { position: absolute; left: 0; top: 0; }

  /* Contact slide */
  .contact { top: 2501px; }
  .contact-photo { left: 31px; top: 109px; width: 528px; height: 299px; background: linear-gradient(180deg, #b9a6cf 0%, #d6b3c8 30%, #c7a27a 60%, #d8b24a 78%, #4f7f86 100%); }
  .contact-list { position: absolute; left: 578px; top: 104px; width: 363px; }
  .contact-person { height: 81px; padding: 8px 0 0 68px; font-size: 13.5px; line-height: 24px; color: var(--ink); border-bottom: 1.5px solid #555; }
  .contact-person:last-child { border-bottom: none; }
  .disclaimer-title { position: absolute; left: 31px; top: 444px; font-family: "Tinos", "Times New Roman", serif; font-size: 19px; font-weight: 400; color: var(--title-green); }
  .disclaimer-text { position: absolute; left: 31px; top: 474px; width: 940px; font-size: 10.5px; line-height: 15.5px; color: var(--muted); }
</style>
</head>
<body>

<section class="slide intro">
  <h1 class="slide-title">Lorem Ipsum</h1>
  <div class="brand"><span class="brand-dot"></span>Dorelmont Capital</div>
  <div class="intro-panel">
    <div class="intro-icon" style="top:45px">
      <svg width="40" height="40" viewBox="0 0 40 40" fill="#fff">
        <circle cx="12" cy="11" r="4"/><circle cx="20" cy="9" r="4.5"/><circle cx="28" cy="11" r="4"/>
        <rect x="7" y="17" width="10" height="15" rx="3"/><rect x="15" y="15" width="10" height="18" rx="3"/><rect x="23" y="17" width="10" height="15" rx="3"/>
      </svg>
    </div>
    <p class="intro-text" style="top:39px">Our team has over 50 years<br>combined experience in electric<br>vehicle and renewable energy<br>technology, project development,<br>and fund management</p>
    <div class="intro-icon" style="top:170px">
      <svg width="36" height="36" viewBox="0 0 36 36"><path d="M21 3 L8 20 H17 L14 33 L28 14 H19 Z" fill="#fff"/></svg>
    </div>
    <p class="intro-text" style="top:164px">Our first fund, the Fleet Transition<br>Fund Africa, will address typical barriers<br>to EV adoption by providing commercial<br>fleets with vehicles and charging<br>infrastructure, as-a-service</p>
    <div class="intro-icon" style="top:297px">
      <svg width="42" height="42" viewBox="0 0 42 42" fill="none" stroke-width="2.5">
        <circle cx="21" cy="21" r="16" fill="#fff"/>
        <path d="M9 17 C14 14 16 20 20 20 C23 21 21 27 17 30" stroke="#70a33d"/>
        <path d="M26 8 C24 13 30 15 33 18" stroke="#70a33d"/>
      </svg>
    </div>
    <p class="intro-text" style="top:291px">In deploying capital to fast-track EV<br>adoption, Dorelmont Capital will have a<br>meaningful and measurable impact on<br>both people and planet</p>
  </div>
  <div class="photo intro-photo" role="img" aria-label="Photo of a canopy-covered EV charging station with charging posts"></div>
</section>

<section class="slide team">
  <h1 class="slide-title">OUR TEAM</h1>
  <div class="brand"><span class="brand-dot"></span>Dorelmont Capital</div>

  <article class="member" style="left:22px">
    <div class="photo member-photo" role="img" aria-label="Portrait photo of Julian Tredwell" style="background:linear-gradient(160deg,#6a7d9a,#2b3240 60%,#c9c6bd)"></div>
    <p class="member-name">Julian Tredwell<br>Partner</p>
    <p class="member-bio">Julian is an accomplished multinational business and sustainable finance professional. His career started with ten years on the general management fast track at Ardent Press, an FT100 listed multinational. Julian went on to spend fifteen years in sustainable finance structuring, marketing, managing and investing sustainable and impact PE and VC investment funds.</p>
  </article>

  <article class="member" style="left:266px">
    <div class="photo member-photo" role="img" aria-label="Landscape photo of a snow-capped mountain with autumn leaves" style="background:linear-gradient(180deg,#3c5d86,#8aa1bb 50%,#5a4a44 75%,#7a2a22)"></div>
    <p class="member-name">Kenji Arakawa<br>Partner</p>
    <p class="member-bio">Kenji is a seasoned banker and investor with cross sectoral expertise in finance. Kenji has a proven track record in Infrastructure investing, Corporate Finance, Trading and Asset Liability Management, Fund of Funds, Securitization and Equity Finance investment. Kenji spent 10 years as Principal at Keystone Ventures in London, investing in fuel cell companies globally.</p>
  </article>

  <article class="member" style="left:511px">
    <div class="photo member-photo" role="img" aria-label="Portrait photo of Marcus Halden" style="background:linear-gradient(160deg,#2a2f36,#9a7a68 50%,#3c4a3a)"></div>
    <p class="member-name">Marcus Halden<br>Partner</p>
    <p class="member-bio">Marcus is an accomplished renewable energy and real estate entrepreneur and investor. After seven years as VP of sales at a large importing business, Marcus founded and has spent 12 years managing a leading US solar energy, energy efficiency and vehicle charging installer. Marcus has managed the launch of an EV fleet and charging infrastructure for Norcar Rentals, and for the City of Easton including Police, Fire, Parks and Sanitation departments.</p>
  </article>

  <article class="member" style="left:757px">
    <div class="photo member-photo" role="img" aria-label="Portrait photo of Helena Lindqvist" style="background:linear-gradient(160deg,#d8d2c6,#c9b08a 45%,#e7e2d8)"></div>
    <p class="member-name">Helena Lindqvist<br>Consultant</p>
    <p class="member-bio">Helena brings a background in engineering, project management, and infrastructure advisory. She started her career as a civil engineer at New Zealand's largest consultancy, during which time she developed a keen interest in sustainability and drove company-wide change programmes. As an engineer, Helena specialised in contract preparation, project mangement, and creating programme business cases for public and private infrastructure investment.</p>
  </article>
</section>

<section class="slide projects">
  <h1 class="slide-title">Our Projects</h1>
  <div class="brand"><span class="brand-dot"></span>Dorelmont Capital</div>
  <div class="photo projects-photo" role="img" aria-label="Photo of a busy city street with minibuses and pedestrians"></div>
  <h2 class="sub-heading" style="left:523px;top:118px">What types of projects do we invest in?</h2>
  <ul class="bullets">
    <li>The project enables owners and operators of commercial fleets (such as buses, trucks, taxis) to reduce or avoid emissions by the adoption of cleaner technologies. This could include the purchase of plug-in electric or hydrogen vehicles, the retrofitting of existing vehicles, and the installation of charging infrastructure</li>
    <li>The project has a high climate and health impact potential, and a measurable impact at city and regional levels</li>
    <li>The project aligns with our investment principles, and our environmental management systems</li>
    <li>The project is expected to provide attractive financial return</li>
  </ul>
  <p class="projects-note">At least 60% of our fund is expected to finance projects in Southern and Sub-Saharan Africa, with the balance being deployed in OECD countries.</p>
</section>

<section class="slide partner">
  <h1 class="slide-title">Our Projects</h1>
  <div class="brand"><span class="brand-dot"></span>Dorelmont Capital</div>
  <h2 class="sub-heading" style="left:51px;top:146px">Why partner with us?</h2>
  <ul class="bullets">
    <li>Access to up-front capital to enable your organisation's fleet electrification, with repayment on a per-mile or per-kWh basis (commercial agreement will vary project-by-project)</li>
    <li>Our understanding of the fast-changing landscape of green road transport technologies, as well as the business models and funding mechanisms which can be applied to reduce technological risks and uncertainty</li>
    <li>Our network of partner organisations with aligned objectives, benefiting from knowledge sharing and leveraging efficiencies</li>
  </ul>
  <svg class="bar-chart" width="1002" height="563" viewBox="0 0 1002 563" font-family="Noto Sans, Verdana, sans-serif" font-size="9" fill="#333">
    <rect x="484" y="157" width="479" height="286" fill="#f0efed"/>
    <g text-anchor="end">
      <text x="475" y="166">800</text><text x="475" y="200">700</text><text x="475" y="233">600</text>
      <text x="475" y="267">500</text><text x="475" y="301">400</text><text x="475" y="335">300</text>
      <text x="475" y="369">200</text><text x="475" y="403">100</text><text x="469" y="437">0</text>
    </g>
    <g fill="#70a33d">
      <rect x="488" y="400" width="24" height="34"/>
      <rect x="518" y="390" width="24" height="44"/>
      <rect x="552" y="373" width="24" height="61"/>
      <rect x="588" y="359" width="24" height="75"/>
      <rect x="623" y="319" width="24" height="115"/>
      <rect x="660" y="285" width="24" height="149"/>
      <rect x="691" y="210" width="24" height="224"/>
      <rect x="725" y="285" width="24" height="149"/>
      <rect x="761" y="295" width="24" height="139"/>
      <rect x="797" y="312" width="24" height="122"/>
      <rect x="826" y="332" width="24" height="102"/>
      <rect x="862" y="305" width="24" height="129"/>
      <rect x="897" y="356" width="24" height="78"/>
      <rect x="926" y="380" width="24" height="54"/>
    </g>
    <g text-anchor="middle" font-size="8.5">
      <text x="500" y="456">1</text><text x="530" y="456">2</text><text x="564" y="456">3</text>
      <text x="600" y="456">4</text><text x="635" y="456">5</text><text x="672" y="456">6</text>
      <text x="703" y="456">7</text><text x="737" y="456">8</text><text x="773" y="456">9</text>
      <text x="809" y="456">10</text><text x="838" y="456">11</text><text x="874" y="456">12</text>
      <text x="909" y="456">13</text><text x="938" y="456">14</text>
    </g>
  </svg>
</section>

<section class="slide contact">
  <h1 class="slide-title">Contact Us</h1>
  <div class="brand"><span class="brand-dot"></span>Dorelmont Capital</div>
  <div class="photo contact-photo" role="img" aria-label="Photo of a lakeside old town with a church spire and lit bridge at dusk"></div>
  <div class="contact-list">
    <div class="contact-person">Julian Tredwell<br>Phone: +41 79000 4817<br>Email: julian@dorelmont.capital</div>
    <div class="contact-person" style="padding-top:22px">Kenji Arakawa<br>Email: kenji@dorelmont.capital</div>
    <div class="contact-person" style="padding-top:20px">Marcus Halden<br>Email: marcus@dorelmont.capital</div>
    <div class="contact-person" style="padding-top:20px">Helena Lindqvist<br>Email: helena@dorelmont.capital</div>
  </div>
  <h2 class="disclaimer-title">Disclaimer</h2>
  <p class="disclaimer-text">Sed ut perspiciatis unde omnis iste natus error sit voluptatem accusantium doloremque laudantium, totam rem aperiam, eaque ipsa quae ab illo inventore veritatis et quasi architecto beatae vitae dicta sunt explicabo. Nemo enim ipsam voluptatem quia voluptas sit aspernatur aut odit aut fugit, sed quia consequuntur magni dolores eos qui ratione voluptatem sequi nesciunt. Neque porro quisquam est, qui dolorem ipsum quia dolor sit amet, consectetur, adipisci velit, sed quia non numquam eius modi tempora incidunt ut labore et dolore magnam aliquam quaerat voluptatem. Ut enim ad minima veniam, quis nostrum exercitationem</p>
</section>

</body>
</html>
```